TRK - Brochure 52 week Curriculum

Tide Rise Kin, Inc. wants to create a distribution Brochure. In the Bible (Matthew 28:18-20)- JESUS said to "TEACH" others what HE has commanded. we want to "PUT IN PRINT"

these 52 lines summarize HIS teachings
we want to use as our Curriculum teaching men ...

incorporate our statements and two main passages of scripture
(see attach pictures of headquarter lobby) to brand uniformity and consistency... we have summarized into 52 groups, but its NOT required to have numbers...
Purpose = obey GOD
Mission = love others
Vision = Development God fearing men globally.

The designer can have freedom in layout and sizing.
we were thinking bi fold , but again... designer has freedom
Please incorporate our colors (white, black, gray) using color wheel provided and our LOGO with website.

```html
<!DOCTYPE html>
<html lang="en">
<head>
<meta charset="utf-8">
<title>Tide Rise Kin – 52-Week Curriculum Brochure</title>
<link href="https://fonts.googleapis.com/css2?family=Montserrat:ital,wght@0,400;0,500;0,600;0,700;0,800;1,500;1,700&display=swap" rel="stylesheet">
<style>
:root{
  --black:#0d0d0d;
  --ink:#1a1a1a;
  --white:#ffffff;
  --paper:#f7f7f7;
  --gray-light:#e3e3e3;
  --gray:#b5b5b5;
  --gray-dark:#7a7a7a;
  --backdrop:#dedede;
  --glow:#f4c06a;
  --amber:#b5652a;
}
*{margin:0;padding:0;box-sizing:border-box}
html,body{width:837px;height:1200px;overflow:hidden}
body{background:var(--backdrop);font-family:"Montserrat",Arial,sans-serif;color:var(--ink)}
.canvas{position:relative;width:837px;height:1200px}
.spread{position:absolute;left:20px;width:797px;height:560px;display:flex;box-shadow:0 6px 18px rgba(0,0,0,.25)}
.spread--outside{top:24px}
.spread--inside{top:612px}
.page{position:relative;width:398.5px;height:560px;overflow:hidden}

/* shared list styling */
.section-pill{display:block;width:max-content;max-width:92%;margin:8px auto 5px;background:var(--black);color:var(--white);font-weight:700;font-size:8px;line-height:1.2;padding:3px 14px;border-radius:4px;text-align:center}
.teachings{list-style:none;padding:0 20px}
.teaching{display:flex;gap:5px;align-items:flex-start;font-size:5.6px;line-height:7.2px;padding:2px 0 3px;border-bottom:.5px solid var(--gray-light)}
.teaching b{font-weight:700}
.teaching-num{flex:none;width:9px;height:9px;border-radius:50%;background:var(--black);color:var(--white);font-size:4.6px;font-weight:700;display:flex;align-items:center;justify-content:center;margin-top:-.5px}

/* back page */
.page--back{background:linear-gradient(180deg,var(--white) 0%,#efefef 55%,#cfcfcf 100%);display:flex;flex-direction:column}
.page--back .contents{flex:1;padding-top:10px;overflow:hidden}
.page--back .section-pill{margin:5px auto 3px;padding:2.5px 14px}
.page--back .teaching{padding:1.5px 0 2px}
.back-footer{flex:none;height:100px;background:linear-gradient(180deg,#c9c9c9,#b3b3b3);padding:12px 24px}
.back-footer .invite{font-size:7px;font-style:italic;font-weight:500;color:var(--ink)}
.back-footer .invite span{color:var(--white);font-weight:700}
.footer-row{display:flex;justify-content:space-between;align-items:flex-end;margin-top:10px}
.brand-name{font-weight:800;color:var(--black);letter-spacing:.5px;display:block}
.back-brand .brand-name{font-size:22px;line-height:1}
.back-brand .site{font-size:6.5px;font-weight:700;margin-top:4px;display:block}
.contact-list{list-style:none}
.contact-item{display:flex;align-items:center;gap:6px;margin-bottom:4px}
.contact-item svg{width:11px;height:11px;flex:none}
.contact-label{font-size:6.5px;font-weight:700;display:block;line-height:1.1}
.contact-value{font-size:6.5px;display:block;line-height:1.1}

/* cover */
.page--cover{background:var(--black);color:var(--white);text-align:center}
.cover-brand{padding-top:26px}
.cover-brand .brand-name{color:var(--white);font-size:18px;letter-spacing:1px}
.cover-title{font-size:17px;font-weight:800;margin-top:16px}
.cover-sub{font-size:7.5px;font-weight:500;margin-top:2px;color:#ddd}
.cover-image{position:absolute;left:0;right:0;top:120px;height:300px;background:radial-gradient(ellipse 38% 46% at 50% 42%,#fff2cf 0%,var(--glow) 22%,var(--amber) 48%,#3a2418 72%,var(--black) 100%)}
.cover-tagline{position:absolute;left:0;right:0;top:432px;font-size:11.5px;font-weight:800}
.cover-scripture{position:absolute;left:36px;right:36px;top:452px;font-size:5.6px;line-height:7.2px;color:#d8d8d8}
.cover-ref{display:block;font-weight:700;color:var(--white);margin-top:4px}
.cover-site{position:absolute;left:0;right:0;bottom:22px;font-size:6.5px;font-weight:700}

/* inside */
.page--inside-left{background:var(--paper)}
.page--inside-right{background:var(--paper);border-left:.5px solid var(--gray-light)}
.identity-band{background:var(--black);color:var(--white);padding:16px 18px 22px;height:148px}
.statements{display:flex;align-items:center}
.statement{flex:1;text-align:center;border-right:.5px solid #555;padding:2px 4px}
.statement:last-child{border-right:none}
.statement strong{display:block;font-style:italic;font-weight:700;font-size:10px;line-height:1.15}
.statement em{display:block;font-style:italic;font-weight:500;font-size:7px;color:#cfcfcf;margin-top:3px}
.band-scripture{font-size:5.6px;line-height:7.2px;color:#cfcfcf;text-align:center;margin:14px 10px 0}
.band-scripture .ref{display:block;font-weight:700;color:var(--white);font-size:7px;margin-top:2px}
.page--inside-left .first-pill{margin-top:-12px;position:relative}
.page--inside-right .teachings{padding-top:14px}
</style>
</head>
<body>
<div class="canvas">

  <section class="spread spread--outside">
    <article class="page page--back">
      <div class="contents">
        <h3 class="section-pill">Living as a Disciple</h3>
        <ol class="teachings">
          <li class="teaching"><span class="teaching-num">37</span><p><b>Be merciful:</b> Show compassion to others, just as God is merciful. Act with kindness and compassion towards others. Luke 6:36</p></li>
          <li class="teaching"><span class="teaching-num">38</span><p><b>Care for those in distress:</b> Help the hungry, thirsty, strangers, naked, sick, and imprisoned.</p></li>
          <li class="teaching"><span class="teaching-num">39</span><p>Recognize your own imperfections and avoid judging others harshly. Matthew 7:1-2, Luke 6:37. The standard by which you judge will be applied to you.</p></li>
          <li class="teaching"><span class="teaching-num">40</span><p><b>Seek God's kingdom first:</b> Make God and his righteousness your highest priority. Found in Matthew 6:33.</p></li>
          <li class="teaching"><span class="teaching-num">41</span><p><b>Abide in JESUS:</b> John 15:4, John 6:35, 40, 47, John 14:27.</p></li>
          <li class="teaching"><span class="teaching-num">42</span><p><b>Follow JESUS:</b> Matthew 4:19, Luke 5:28</p></li>
        </ol>
        <h3 class="section-pill">Forgiveness (Jesus taught about the importance of both receiving and giving forgiveness)</h3>
        <ol class="teachings">
          <li class="teaching"><span class="teaching-num">43</span><p><b>Forgive others:</b> Matthew 6:12, 14, Mark 11:25-26, Luke 6:37</p></li>
          <li class="teaching"><span class="teaching-num">44</span><p>JESUS emphasized that forgiveness is linked to forgiving others (Matthew 6:14-15)</p></li>
          <li class="teaching"><span class="teaching-num">45</span><p>Forgiveness should be extended limitlessly to those who repent (Luke 17:3-4; Matthew 18:21-22).</p></li>
          <li class="teaching"><span class="teaching-num">46</span><p>Forgiveness is also illustrated as the cancellation of debt (Matthew 18:21-35).</p></li>
        </ol>
        <h3 class="section-pill">Humility and Service</h3>
        <ol class="teachings">
          <li class="teaching"><span class="teaching-num">47</span><p>JESUS stated that humility leads to being honored (Luke 14:11; Matthew 23:12)</p></li>
          <li class="teaching"><span class="teaching-num">48</span><p>True greatness is found in serving others (Matthew 20:26-28).</p></li>
          <li class="teaching"><span class="teaching-num">49</span><p>The Bible also states that God opposes the proud but shows favor to the humble (James 4:6; 1 Peter 5:5).</p></li>
        </ol>
        <h3 class="section-pill">Warning against self-righteousness and judgment</h3>
        <ol class="teachings">
          <li class="teaching"><span class="teaching-num">50</span><p>Jesus warned against hypocrisy, particularly the hypocrisy of the Pharisees (Luke 12:1).</p></li>
        </ol>
        <h3 class="section-pill">Money (Jesus taught about using money and possessions responsibly)</h3>
        <ol class="teachings">
          <li class="teaching"><span class="teaching-num">51</span><p>JESUS advised storing up treasures in Heaven rather than on Earth (Matthew 6:19-21)</p></li>
          <li class="teaching"><span class="teaching-num">52</span><p>JESUS stated that it is impossible to serve both God and money (Matthew 6:24).</p></li>
        </ol>
      </div>

      <footer class="back-footer">
        <p class="invite">To learn more about events and community involvement, <span>contact us.</span></p>
        <div class="footer-row">
          <div class="back-brand">
            <span class="brand-name">TRK</span>
            <span class="site">WWW.TIDERISEKIN.COM</span>
          </div>
          <ul class="contact-list">
            <li class="contact-item">
              <svg viewBox="0 0 12 12"><circle cx="6" cy="6" r="5.5" fill="none" stroke="#0d0d0d" stroke-width=".8"/><path d="M4.2 3.3l1 1-.6.7c.4.9 1 1.5 1.9 1.9l.7-.6 1 1-.8.9c-2 -.3-3.8-2.1-4.1-4.1z" fill="#0d0d0d"/></svg>
              <div><span class="contact-label">Phone</span><span class="contact-value">555-014-2290</span></div>
            </li>
            <li class="contact-item">
              <svg viewBox="0 0 12 12"><circle cx="6" cy="6" r="5.5" fill="none" stroke="#0d0d0d" stroke-width=".8"/><rect x="3.2" y="4" width="5.6" height="4" fill="none" stroke="#0d0d0d" stroke-width=".7"/><path d="M3.2 4l2.8 2.2L8.8 4" fill="none" stroke="#0d0d0d" stroke-width=".7"/></svg>
              <div><span class="contact-label">Email</span><span class="contact-value">info@tiderisekin.com</span></div>
            </li>
            <li class="contact-item">
              <svg viewBox="0 0 12 12"><circle cx="6" cy="6" r="5.5" fill="none" stroke="#0d0d0d" stroke-width=".8"/><path d="M6 9.2S3.9 6.9 3.9 5.3a2.1 2.1 0 0 1 4.2 0C8.1 6.9 6 9.2 6 9.2z" fill="#0d0d0d"/><circle cx="6" cy="5.3" r=".7" fill="#fff"/></svg>
              <div><span class="contact-label">Address</span><span class="contact-value">Millbrook, Georgia, US</span></div>
            </li>
          </ul>
        </div>
      </footer>
    </article>

    <article class="page page--cover">
      <div class="cover-brand"><span class="brand-name">Tide Rise Kin</span></div>
      <h1 class="cover-title">52-Week Curriculum</h1>
      <p class="cover-sub">Teaching what Jesus commanded.</p>
      <div class="cover-image" role="img" aria-label="Photograph of a robed figure walking out of a cave entrance toward a bright sunrise over distant mountains"></div>
      <h2 class="cover-tagline">Develop God Fearing Men Globally</h2>
      <p class="cover-scripture">Then Jesus came to them and said, "All authority in heaven and on earth has been given to me. Therefore go and make disciples of all nations, baptizing them in the name of the Father and of the Son and of the Holy Spirit, and teaching them to obey everything I have commanded you. And surely I am with you always, to the very end of the age."<span class="cover-ref">Matthew 28:18-20</span></p>
      <p class="cover-site">WWW.TIDERISEKIN.COM</p>
    </article>
  </section>

  <section class="spread spread--inside">
    <article class="page page--inside-left">
      <header class="identity-band">
        <div class="statements">
          <div class="statement"><strong>Obey God</strong><em>Our Purpose</em></div>
          <div class="statement"><strong>Love Others</strong><em>Our Mission</em></div>
          <div class="statement"><strong>Development God fearing men globally.</strong><em>Our Vision</em></div>
        </div>
        <p class="band-scripture">Jesus replied: "Love the Lord your God with all your heart and with all your soul and with all your mind. This is the first and greatest commandment. And the second is like it: 'Love your neighbor as yourself.' All the Law and the Prophets hang on these two commandments."<span class="ref">Matthew 22:37-40</span></p>
      </header>
      <h3 class="section-pill first-pill">Regarding God and righteousness</h3>
      <ol class="teachings">
        <li class="teaching"><span class="teaching-num">01</span><p><b>Repent:</b> Change your mind and actions towards sin, as the Kingdom of Heaven is near. Turn away from sin and toward GOD. Matthew 4:17, Luke 13:3. Found in Mark 1:15.</p></li>
        <li class="teaching"><span class="teaching-num">02</span><p>Accept the Good News of salvation offered through Jesus.</p></li>
        <li class="teaching"><span class="teaching-num">03</span><p><b>Believe in the Son of God, Jesus Christ:</b> This is essential for salvation and receiving the Holy Spirit. John 6:29, John 14:11</p></li>
        <li class="teaching"><span class="teaching-num">04</span><p>Have faith in God, and trust in Jesus as the Son of God.</p></li>
        <li class="teaching"><span class="teaching-num">05</span><p><b>Be born again:</b> John 3:7 Be born again (of water and the Spirit): Experience a spiritual transformation necessary for entrance into God's Kingdom.</p></li>
        <li class="teaching"><span class="teaching-num">06</span><p>Give your utmost devotion and affection to God. Love God with all your heart, soul, mind, and strength: Matthew 22:37-38, Mark 12:30, Luke 10:27</p></li>
        <li class="teaching"><span class="teaching-num">07</span><p><b>Honor God's Law:</b> Understand that Jesus did not come to abolish the Law but to fulfill it and to magnify its application in the heart.</p></li>
      </ol>
      <h3 class="section-pill">Regarding relationships and ethics</h3>
      <ol class="teachings">
        <li class="teaching"><span class="teaching-num">08</span><p><b>Love your Neighbor as yourself:</b> Matthew 22:39, Mark 12:31, Luke 10:27, Leviticus 19:18. Love one another, as I have loved you.</p></li>
        <li class="teaching"><span class="teaching-num">09</span><p><b>The Golden Rule:</b> Treat others as you would want to be treated. (Matthew 7:12).</p></li>
        <li class="teaching"><span class="teaching-num">10</span><p><b>Be reconciled to your brother:</b> Seek peace and forgiveness when relationships are broken.</p></li>
        <li class="teaching"><span class="teaching-num">11</span><p><b>Go to those who offend you:</b> Address offenses directly and privately before involving others.</p></li>
        <li class="teaching"><span class="teaching-num">12</span><p><b>Forgive offenders:</b> Extend forgiveness to those who hurt you and forgive often.</p></li>
        <li class="teaching"><span class="teaching-num">13</span><p><b>Love your enemies and pray for those who persecute you:</b> Matthew 5:44, Luke 6:27-28.</p></li>
      </ol>
      <h3 class="section-pill">Regarding personal conduct and Attitudes</h3>
      <ol class="teachings">
        <li class="teaching"><span class="teaching-num">14</span><p><b>Be baptized:</b> Be immersed in water as a symbol of your new life in Christ.</p></li>
        <li class="teaching"><span class="teaching-num">15</span><p><b>Take, eat, and drink in remembrance of Me (Communion/Lord's Supper):</b> Participate in the commemoration of Jesus' sacrifice.</p></li>
      </ol>
    </article>

    <article class="page page--inside-right">
      <ol class="teachings">
        <li class="teaching"><span class="teaching-num">16</span><p><b>Let your light shine before others:</b> Matthew 5:16. Live so that your good deeds bring glory to GOD.</p></li>
        <li class="teaching"><span class="teaching-num">17</span><p><b>Care for the less fortunate:</b> Help those in need, such as the hungry, thirsty, strangers, naked, sick, and imprisoned. Luke 14:13-14, Matthew 25:31-46.</p></li>
        <li class="teaching"><span class="teaching-num">18</span><p><b>Deny yourself, Take up your cross daily and follow Jesus:</b> A commitment to discipleship, even in hardship. Luke 9:23-24; Matthew 16:24-25.</p></li>
        <li class="teaching"><span class="teaching-num">19</span><p><b>Fast:</b> Engage in fasting, but do so for the right reasons and not for outward show.</p></li>
        <li class="teaching"><span class="teaching-num">20</span><p><b>Be wise as serpents and innocent as doves:</b> Matthew 10:16</p></li>
        <li class="teaching"><span class="teaching-num">21</span><p><b>Do not worry about your life or material possessions:</b> Trust God to provide for your needs. Matthew 6:34</p></li>
        <li class="teaching"><span class="teaching-num">22</span><p><b>Lay up treasures in heaven:</b> Focus on a spiritual inheritance rather than earthly wealth. Matthew 6:19-21</p></li>
        <li class="teaching"><span class="teaching-num">23</span><p><b>Be a servant:</b> Seek greatness through humble service to others. Matthew 20:25-28</p></li>
      </ol>
      <h3 class="section-pill">Prayer</h3>
      <ol class="teachings">
        <li class="teaching"><span class="teaching-num">24</span><p>Jesus provided guidance on prayer, teaching that it should be done in private and with sincerity (Matthew 6:5-8).</p></li>
        <li class="teaching"><span class="teaching-num">25</span><p>He also linked prayer to having a forgiving heart (Mark 11:25; Matthew 18:18-20) and simple faith (Luke 11:5-13).</p></li>
        <li class="teaching"><span class="teaching-num">26</span><p><b>Pray:</b> Engage in prayer consistently, with sincerity and according to Jesus' example.</p></li>
        <li class="teaching"><span class="teaching-num">27</span><p><b>Prayer for our enemies :</b> Luke 23:24, Matthew 5:44</p></li>
        <li class="teaching"><span class="teaching-num">28</span><p><b>Pray for others :</b> intercession</p></li>
        <li class="teaching"><span class="teaching-num">29</span><p><b>Pray for laborers:</b> Seek God to send workers into the harvest field of souls. Matthew 9:38, Luke 10:2</p></li>
      </ol>
      <h3 class="section-pill">Regarding outreach and discipleship</h3>
      <ol class="teachings">
        <li class="teaching"><span class="teaching-num">30</span><p><b>Go and make disciples of all nations:</b> Evangelize and teach others to follow Jesus' commands. Matthew 28:18-20.</p></li>
        <li class="teaching"><span class="teaching-num">31</span><p><b>Feed My Sheep:</b> Care for and nourish the spiritual lives of believers.</p></li>
        <li class="teaching"><span class="teaching-num">32</span><p><b>Receive God's power:</b> Be filled with the Holy Spirit to effectively carry out God's work.</p></li>
      </ol>
      <h3 class="section-pill">Cautions and warnings</h3>
      <ol class="teachings">
        <li class="teaching"><span class="teaching-num">33</span><p><b>Beware of false prophets:</b> Be discerning and recognize those who may mislead others with false teachings.</p></li>
        <li class="teaching"><span class="teaching-num">34</span><p><b>Beware of leaven (doctrine) of the Pharisees and Sadducees:</b> Avoid hypocrisy and legalism.</p></li>
        <li class="teaching"><span class="teaching-num">35</span><p>Be alert and reliant on God's strength to overcome temptation.</p></li>
        <li class="teaching"><span class="teaching-num">36</span><p><b>Do not cast pearls before swine:</b> Use discretion with those who may devalue or disrespect them.</p></li>
      </ol>
    </article>
  </section>

</div>
</body>
</html>
```